ServLoom Website Homepage Design

Please provide your idea of homepage for a hosting company. This project is for DESIGN only, no coding.

It must use/combine colors used in logo, clean, modern look.

Homepage must consist of at least 4 sections (example: testimonials, services, and so on. not necesarily all of them). We would like the navigation to be horizontal, but not mandatory.

You can include a preview of services page (optional, not a must).

Number of Pages Required

1 page

Font styles to use
Sans Serif

```html
<!DOCTYPE html>
<html lang="en">
<head>
<meta charset="utf-8">
<title>ServLoom — Hosting Company</title>
<link href="https://fonts.googleapis.com/css2?family=Lato:wght@400;700;900&display=swap" rel="stylesheet">
<style>
:root{
  --blue:#0f6fd2;
  --blue-bright:#1a7de0;
  --ink:#2e2e2e;
  --text:#444;
  --band:#dce9f7;
  --grey:#efefef;
  --footer:#2a2a2a;
  --footer-text:#d6d6d6;
  --white:#fff;
}
*{margin:0;padding:0;box-sizing:border-box}
html,body{width:1200px;height:4017px;overflow:hidden}
body{font-family:'Lato',sans-serif;color:var(--text);background:var(--white);position:relative}
.abs{position:absolute}
section,header,footer{position:absolute;left:0;width:1200px}

/* header */
.site-header{top:0;height:151px;background:var(--white)}
.brand{left:78px;top:56px;font-size:50px;font-weight:900;color:var(--blue);letter-spacing:1px;line-height:54px}
.main-nav{right:73px;top:73px;display:flex;gap:44px}
.main-nav a{font-size:15px;font-weight:900;color:var(--ink);text-decoration:none;letter-spacing:.3px}
.main-nav a.active{color:var(--blue)}

/* hero */
.hero{top:151px;height:793px;background:radial-gradient(ellipse at 35% 45%,#2b4f8c 0%,#142a55 45%,#0a1630 100%);
  clip-path:polygon(0 0,100% 0,100% 629px,50% 100%,0 629px)}
.hero-copy{right:73px;top:215px;text-align:right;color:var(--white)}
.hero-title{font-size:53px;font-weight:900;line-height:60px;letter-spacing:.5px}
.hero-sub{font-size:37px;font-weight:700;line-height:44px;margin-top:6px}
.btn{display:inline-block;background:var(--blue-bright);color:var(--white);font-weight:900;font-size:17px;border-radius:24px;text-align:center;line-height:48px;text-decoration:none}
.hero .btn{position:absolute;right:73px;top:392px;width:191px}

/* common headings */
.sec-title{width:1200px;left:0;text-align:center;font-size:44px;font-weight:900;color:var(--blue);line-height:50px}
.sec-lead{width:1200px;left:0;text-align:center;font-size:16px;color:var(--text)}
.eyebrow{width:1200px;left:0;text-align:center;font-size:31px;color:var(--blue);line-height:36px}

/* services */
.services{top:944px;height:635px}
.service-card{top:237px;width:330px;height:316px;background:var(--white);border-radius:6px;box-shadow:0 2px 14px rgba(0,0,0,.12);text-align:center;padding-top:38px}
.service-card.featured{background:var(--blue-bright);color:var(--white);box-shadow:none}
.service-card svg{display:block;margin:0 auto;height:70px}
.service-card h3{margin-top:34px;font-size:22px;font-weight:900;color:var(--blue)}
.service-card.featured h3{color:var(--white)}
.service-card p{margin:8px auto 0;width:270px;font-size:16px;line-height:28px}

/* about */
.about{top:1579px;height:512px;background:var(--band)}
.about-kicker{left:75px;top:98px;font-size:31px;color:var(--ink)}
.about-title{left:75px;top:140px;font-size:46px;font-weight:900;color:var(--blue)}
.about-text{left:75px;top:206px;width:520px;font-size:16px;line-height:33px}
.about .btn{position:absolute;left:75px;top:358px;width:189px}
.about-art{left:609px;top:99px;width:538px;height:335px;border-radius:48% 52% 40% 60%/55% 45% 55% 45%;background:radial-gradient(ellipse at 50% 50%,#a9c7ea 0%,#c6dbf2 60%,#dce9f7 100%)}

/* testimonials */
.testimonials{top:2091px;height:445px;z-index:2}
.avatar{left:526px;top:144px;width:150px;height:150px;border-radius:50%;background:radial-gradient(circle at 50% 40%,#e4e4e4 0%,#c9c9c9 70%,#b8b8b8 100%)}
.quote-mark{left:615px;top:240px;font-size:120px;font-weight:900;color:var(--blue);line-height:100px}
.arrow{top:198px}
.quote{width:1200px;left:0;top:318px;text-align:center;font-size:16px;line-height:36px;color:var(--text)}
.quote-name{width:1200px;left:0;top:448px;text-align:center;font-size:17px;font-weight:700;color:var(--blue)}

/* blog */
.blog{top:2536px;height:1084px;background:var(--grey);z-index:1}
.blog-notch{left:0;top:0;width:1200px;height:164px}
.post{top:405px;width:330px;height:511px;background:var(--white);border-radius:8px;box-shadow:0 2px 12px rgba(0,0,0,.08);overflow:hidden}
.post-img{height:230px}
.post-body{padding:24px 24px 0}
.post-date{font-size:15px;font-weight:900;color:var(--blue)}
.post h3{margin-top:10px;font-size:25px;font-weight:700;color:var(--ink);line-height:32px}
.post p{margin-top:8px;font-size:16px;line-height:28px}
.post a{display:block;margin-top:16px;font-size:15px;font-weight:900;color:var(--blue);text-decoration:none}
.dots{left:553px;top:980px;display:flex;gap:13px}
.dots span{width:13px;height:13px;border-radius:50%;background:var(--ink)}
.dots span.on{background:var(--blue-bright)}

/* footer */
.site-footer{top:3620px;height:397px;background:var(--footer);color:var(--footer-text)}
.foot-brand{left:75px;top:143px;font-size:40px;font-weight:900;color:var(--blue);line-height:44px}
.copy{left:75px;top:200px;font-size:13px;line-height:26px}
.divider{top:63px;width:1px;height:273px;background:#4a4a4a}
.foot-col h4{font-size:18px;font-weight:900;color:var(--white);letter-spacing:.3px}
.foot-col ul{list-style:none;margin-top:12px}
.foot-col li{font-size:14px;line-height:34.5px}
.contact-list li{display:flex;gap:14px;align-items:flex-start;font-size:16px;line-height:34px}
.contact-list svg{width:18px;height:18px;margin-top:8px;flex:none}
.socials{left:884px;top:258px;display:flex;gap:18px}
.socials span{width:18px;height:18px;border-radius:50%;background:var(--white)}
</style>
</head>
<body>

<header class="site-header">
  <div class="brand abs">ServLoom</div>
  <nav class="main-nav abs">
    <a class="active" href="#">HOME</a>
    <a href="#">WHO WE ARE</a>
    <a href="#">WHAT WE DO</a>
    <a href="#">TESTIMONIALS</a>
    <a href="#">CONTACT</a>
  </nav>
</header>

<section class="hero" role="img" aria-label="Photo of two engineers with a laptop inspecting server racks in a data centre">
  <div class="hero-copy abs">
    <h1 class="hero-title">WELCOME TO SERVLOOM</h1>
    <p class="hero-sub">We are a hosting company<br>from Romania</p>
  </div>
  <a class="btn" href="#">READ MORE</a>
</section>

<section class="services">
  <h2 class="sec-title abs" style="top:86px">OUR SERVICES</h2>
  <p class="sec-lead abs" style="top:152px">Sed ut perspiciatis unde omnis iste natus error sit&nbsp; voluptatem accusantium doloremque laudantium, totam rem aperiam.</p>

  <article class="service-card abs" style="left:75px">
    <svg viewBox="0 0 70 60" aria-hidden="true">
      <g fill="#555"><rect x="0" y="0" width="70" height="16" rx="3"/><rect x="0" y="22" width="70" height="16" rx="3"/><rect x="0" y="44" width="70" height="16" rx="3"/></g>
      <g fill="#fff"><circle cx="54" cy="8" r="2.5"/><circle cx="62" cy="8" r="2.5"/><circle cx="54" cy="30" r="2.5"/><circle cx="62" cy="30" r="2.5"/><circle cx="54" cy="52" r="2.5"/><circle cx="62" cy="52" r="2.5"/></g>
    </svg>
    <h3>DEDICATED SERVER</h3>
    <p>Sed ut perspiciatis unde omnis iste natus error sit&nbsp; voluptatem accusantium doloremque laudantiumtotam.</p>
  </article>

  <article class="service-card featured abs" style="left:435px">
    <svg viewBox="0 0 84 70" aria-hidden="true">
      <rect x="10" y="2" width="64" height="50" rx="4" fill="none" stroke="#fff" stroke-width="5"/>
      <path d="M2 56h80v4a6 6 0 0 1-6 6H8a6 6 0 0 1-6-6z" fill="#fff"/>
      <circle cx="42" cy="27" r="13" fill="none" stroke="#fff" stroke-width="3"/>
      <path d="M29 27h26M42 14v26M33 19c6 3 12 3 18 0M33 35c6-3 12-3 18 0" fill="none" stroke="#fff" stroke-width="2"/>
    </svg>
    <h3>WEB HOSTING</h3>
    <p>Sed ut perspiciatis unde omnis iste natus error sit&nbsp; voluptatem accusantium doloremque laudantiumtotam.</p>
  </article>

  <article class="service-card abs" style="left:796px">
    <svg viewBox="0 0 90 60" aria-hidden="true">
      <path d="M20 60a18 18 0 0 1-2-36 24 24 0 0 1 46-4 20 20 0 0 1 8 40z" fill="#555"/>
    </svg>
    <h3>CLOUD HOSTING</h3>
    <p>Sed ut perspiciatis unde omnis iste natus error sit&nbsp; voluptatem accusantium doloremque laudantiumtotam.</p>
  </article>
</section>

<section class="about">
  <p class="about-kicker abs">Who We Are</p>
  <h2 class="about-title abs">ABOUT COMPANY</h2>
  <p class="about-text abs">Sed ut perspiciatis unde omnis iste natus error sit&nbsp; voluptatem<br>accusantium doloremque laudantium, totam rem&nbsp; aperiam, eaque<br>ipsa quae ab illo inventore veritatis et quasi<br>architecto beatae.</p>
  <a class="btn" href="#">READ MORE</a>
  <div class="about-art abs" role="img" aria-label="Illustration of people working beside server racks and a large dashboard screen with charts"></div>
</section>

<section class="testimonials">
  <h2 class="sec-title abs" style="top:62px">TESTIMONIALS</h2>
  <svg class="arrow abs" style="left:477px" width="22" height="40" viewBox="0 0 22 40" aria-hidden="true"><path d="M19 3L3 20l16 17" fill="none" stroke="#333" stroke-width="3"/></svg>
  <svg class="arrow abs" style="left:703px" width="22" height="40" viewBox="0 0 22 40" aria-hidden="true"><path d="M3 3l16 17L3 37" fill="none" stroke="#333" stroke-width="3"/></svg>
  <div class="avatar abs" role="img" aria-label="Portrait photo of the client"></div>
  <div class="quote-mark abs" aria-hidden="true">&rdquo;</div>
  <p class="quote abs">&ldquo;&nbsp; Sed ut perspiciatis unde omnis iste natus error sit voluptatem accusantium doloremque laudantium, totam rem<br>aperiam, eaque ipsa quae ab illo inventore veritatis et quasi architecto beatae vitae dicta sunt explicabo.<br>Nemo enim ipsam voluptatem quia voluptas sit aspernatur aut odit aut fugi...&rdquo;</p>
  <p class="quote-name abs">NAME HEADING</p>
</section>

<section class="blog">
  <svg class="blog-notch abs" viewBox="0 0 1200 164" preserveAspectRatio="none" aria-hidden="true"><polygon points="0,0 1200,0 600,164" fill="#fff"/></svg>
  <p class="eyebrow abs" style="top:233px">What&rsquo;s New</p>
  <h2 class="sec-title abs" style="top:274px">RECENT BLOG POSTS</h2>
  <p class="sec-lead abs" style="top:339px">Sed ut perspiciatis unde omnis iste natus error sit&nbsp; voluptatem accusantium doloremque laudantium, totam rem aperiam.</p>

  <article class="post abs" style="left:75px">
    <div class="post-img" role="img" aria-label="Photo of a laptop on a server rack shelf" style="background:linear-gradient(135deg,#1a2a4a,#2c5a9a 50%,#0f1a30)"></div>
    <div class="post-body">
      <p class="post-date">JUN18, 2021</p>
      <h3>Sed ut perspiciatis unde omnis iste</h3>
      <p>Nemo enim ipsam voluptatem quia voluptas sit aspernatur aut odit aut fugit, sed quia consequuntur.</p>
      <a href="#">READ MORE</a>
    </div>
  </article>

  <article class="post abs" style="left:435px">
    <div class="post-img" role="img" aria-label="Photo of glowing blue server lights with code overlay" style="background:linear-gradient(135deg,#0d2d5e,#2f7fd6 55%,#0a1c3d)"></div>
    <div class="post-body">
      <p class="post-date">JUN18, 2021</p>
      <h3>Sed ut perspiciatis unde omnis iste</h3>
      <p>Nemo enim ipsam voluptatem quia voluptas sit aspernatur aut odit aut fugit, sed quia consequuntur.</p>
      <a href="#">READ MORE</a>
    </div>
  </article>

  <article class="post abs" style="left:796px">
    <div class="post-img" role="img" aria-label="Photo of a technician with a laptop in a server aisle" style="background:linear-gradient(135deg,#1c1f26,#3a4a66 55%,#14171d)"></div>
    <div class="post-body">
      <p class="post-date">JUN18, 2021</p>
      <h3>Sed ut perspiciatis unde omnis iste</h3>
      <p>Nemo enim ipsam voluptatem quia voluptas sit aspernatur aut odit aut fugit, sed quia consequuntur.</p>
      <a href="#">READ MORE</a>
    </div>
  </article>

  <div class="dots abs"><span class="on"></span><span></span><span></span><span></span></div>
</section>

<footer class="site-footer">
  <div class="foot-brand abs">ServLoom</div>
  <p class="copy abs">Copyright &copy; 2021. Company Name.<br>All Right Reserved</p>

  <div class="divider abs" style="left:342px"></div>
  <div class="divider abs" style="left:599px"></div>
  <div class="divider abs" style="left:855px"></div>

  <div class="foot-col abs" style="left:390px;top:59px">
    <h4>SITE MAP</h4>
    <ul><li>Home</li><li>Who We Are</li><li>What We Do</li><li>Testimonials</li><li>Contact</li></ul>
  </div>

  <div class="foot-col abs" style="left:640px;top:59px">
    <h4>WHAT WE DO</h4>
    <ul><li>Sed ut perspiciatis</li><li>Unde omnis iste</li><li>Natus error sit voluptateA</li><li>ccusantium</li></ul>
  </div>

  <div class="foot-col abs" style="left:882px;top:59px">
    <h4>CONTACT ADDRESS</h4>
    <ul class="contact-list">
      <li><svg viewBox="0 0 18 18" aria-hidden="true"><path d="M9 1a6 6 0 0 0-6 6c0 5 6 10 6 10s6-5 6-10a6 6 0 0 0-6-6z" fill="#fff"/><circle cx="9" cy="7" r="2.2" fill="#2a2a2a"/></svg><span>14 Harbor Lane, Suite Name<br>Lakeview City, USA</span></li>
      <li><svg viewBox="0 0 18 18" aria-hidden="true"><path d="M4 1l3 4-2 2c1 2 3 4 5 5l2-2 4 3-2 3C8 16 2 10 1 4z" fill="#fff"/></svg><span>1-800-555-0199</span></li>
      <li><svg viewBox="0 0 18 18" aria-hidden="true"><rect x="1" y="4" width="16" height="11" rx="1" fill="#fff"/><path d="M1 5l8 6 8-6" fill="none" stroke="#2a2a2a" stroke-width="1.5"/></svg><span>hello@servloom-mail.com</span></li>
    </ul>
  </div>

  <div class="socials abs" aria-label="Social links"><span></span><span></span><span></span><span></span><span></span></div>
</footer>

</body>
</html>
```